Melissa Dorvan Personal Business Card

I like orange. It's would better if my card have an orange background
Address: 5820 Halvers Lane #417
San Jose
California
US
Tel: 4085172049

Industry/Entity Type

Business

```html
<!DOCTYPE html>
<html lang="en">
<head>
<meta charset="utf-8">
<title>Melissa Dorvan — Business Card</title>
<link rel="stylesheet" href="https://fonts.googleapis.com/css2?family=Arvo&family=Libre+Baskerville&display=swap">
<style>
  :root {
    --card-orange: #ff5900;
    --card-orange-glow: #ff6c00;
    --ink: #222222;
  }
  * { margin: 0; padding: 0; box-sizing: border-box; }
  html, body {
    width: 1200px;
    height: 686px;
    overflow: hidden;
  }
  .card {
    position: relative;
    width: 1200px;
    height: 686px;
    background:
      radial-gradient(circle at 0% 100%, var(--card-orange-glow) 0%, rgba(255,108,0,0) 45%),
      var(--card-orange);
    color: var(--ink);
  }
  .card__name {
    position: absolute;
    left: 57px;
    top: 272px;
    font-family: "Libre Baskerville", "Georgia", serif;
    font-size: 62px;
    line-height: 1;
    letter-spacing: 0.5px;
    white-space: nowrap;
  }
  .card__divider {
    position: absolute;
    left: 576px;
    top: 166px;
    width: 3px;
    height: 286px;
    background: var(--ink);
  }
  .card__details {
    position: absolute;
    left: 600px;
    top: 198px;
    font-family: "Arvo", "Rockwell", serif;
    font-size: 38px;
    line-height: 1;
    white-space: nowrap;
  }
  .card__line { display: block; }
  .card__line--street { margin-bottom: 20px; }
  .card__line--city { margin-bottom: 15px; margin-left: -1px; }
  .card__line--region { margin-left: -4px; margin-bottom: 25px; word-spacing: 4px; }
  .card__phone {
    display: flex;
    align-items: center;
    gap: 8px;
  }
  .card__phone-icon { width: 30px; height: 46px; flex: none; }
</style>
</head>
<body>
  <main class="card">
    <h1 class="card__name">Melissa Dorvan</h1>
    <div class="card__divider"></div>
    <address class="card__details" style="font-style: normal;">
      <span class="card__line card__line--street">5820 Halvers Lane #417</span>
      <span class="card__line card__line--city">San Jose</span>
      <span class="card__line card__line--region">California &nbsp;- &nbsp;U S</span>
      <span class="card__line card__phone">
        <svg class="card__phone-icon" viewBox="0 0 30 46" aria-hidden="true">
          <rect x="12" y="0" width="4" height="10" rx="2" fill="#222222"/>
          <rect x="2" y="7" width="26" height="38" rx="6" fill="#222222"/>
          <rect x="7" y="13" width="16" height="11" rx="2" fill="#ff5900"/>
          <circle cx="15" cy="35" r="3.5" fill="#ff5900"/>
        </svg>
        4085172049
      </span>
    </address>
  </main>
</body>
</html>
```